Website Design for Freeze-Dried Food Manufacturing Company (Pet Food & Agri-Food)

We are looking for a high-level web designer to create a clean, modern, premium website design for Tarquel, a freeze-dried food manufacturing company operating in both the pet food and agri-food space.
This is not a basic website build β we are looking for a designer who understands brand positioning, layout, and user flow, not just visuals.
π― Project Objective
Design a website that:
Clearly communicates our capabilities and value proposition
Feels premium, credible, and product-driven
Guides users through a simple, intuitive journey
Clean and Crips
A critical requirement is clearly separating:
π Pet Food
π Agri-Food
These must feel like two distinct pathways within the same brand experience.
We have attached detailed documents outlining structure, layout, and messaging. These should be followed closely.
π What Success Looks Like
A high-impact homepage with strong visual hierarchy
Clear entry points into Pet Food and Agri-Food
Clean, intentional layout (not cluttered or template-like)
Thoughtful spacing, typography, and flow
A design that feels considered and elevated, not generic
π¨ Design Direction
We are aiming for a:
Minimal, premium aesthetic
Warm, natural color palette (creams, browns, muted tones)
Ingredient and product-focused visuals
Avoid:
Overly corporate / industrial styles
Generic SaaS-style layouts
Busy or over-designed interfaces
End Goal
A website that immediately communicates:
Who we are
What we do
Why weβre different
In a way that feels premium, clear, and easy to navigate.
Link to current website: https://tarquelfoods.example/
https://tarquelhealth.example/wp-admin/

```html
<!DOCTYPE html>
<html lang="en">
<head>
<meta charset="utf-8">
<title>Tarquel — Freeze-Dried Pet Food &amp; Agri-Food</title>
<link href="https://fonts.googleapis.com/css2?family=Playfair+Display:wght@400;500;600&family=Manrope:wght@400;500;600;700&display=swap" rel="stylesheet">
<style>
:root{
  --cream:#faf6f1;
  --cream-2:#f3ebe3;
  --sage:#e6ebe6;
  --brown:#6b3f1d;
  --brown-dark:#4a2a12;
  --ink:#2b1d14;
  --muted:#6f6259;
  --line:#e4dcd3;
  --teal:#1f3b3a;
  --white:#ffffff;
}
*{box-sizing:border-box;margin:0;padding:0}
html,body{width:1200px;height:3548px;overflow:hidden}
body{background:var(--cream);color:var(--ink);font-family:"Manrope",sans-serif;position:relative}
.serif{font-family:"Playfair Display",serif}
.eyebrow{font-size:10px;letter-spacing:.18em;text-transform:uppercase;font-weight:700;color:var(--brown)}

/* nav */
.site-nav{position:absolute;top:0;left:0;width:1200px;height:62px;display:flex;align-items:center;padding:0 40px;background:var(--cream)}
.brand{font-family:"Playfair Display",serif;font-size:22px;font-weight:500;letter-spacing:.04em;color:var(--ink)}
.nav-links{position:absolute;left:50%;transform:translateX(-50%);display:flex;gap:34px;font-size:12px;font-weight:500;color:var(--muted)}
.nav-links .active{color:var(--ink);border-bottom:2px solid var(--brown);padding-bottom:4px}
.nav-cta{margin-left:auto;background:var(--brown-dark);color:var(--white);font-size:11px;font-weight:600;padding:8px 16px;border-radius:2px}

/* hero */
.hero{position:absolute;top:62px;left:0;width:1200px;height:840px;display:flex}
.hero-pane{flex:1;position:relative;display:flex;flex-direction:column;align-items:center;justify-content:center;text-align:center;color:var(--white)}
.hero-pet{background:radial-gradient(ellipse at 50% 35%,#c98a3e 0%,#8a5a28 40%,#3b2614 85%)}
.hero-agri{background:linear-gradient(160deg,#9fbdb8 0%,#5f8782 45%,#2f4e4b 100%)}
.hero-pane .eyebrow{color:#f3e6d6;margin-bottom:14px}
.hero-pane h1{font-family:"Playfair Display",serif;font-weight:500;font-size:58px;line-height:1.02;margin-bottom:30px}
.btn-light{background:var(--white);color:var(--ink);font-size:11px;font-weight:600;padding:12px 26px}
.btn-dark{background:var(--teal);color:var(--white);font-size:11px;font-weight:600;padding:12px 26px}

/* difference */
.difference{position:absolute;top:1000px;left:52px;width:1096px}
.difference h2{font-family:"Playfair Display",serif;font-weight:500;font-size:40px;line-height:1.15;margin-top:18px;width:560px}
.difference p{position:absolute;right:0;top:46px;width:360px;font-size:14px;line-height:1.6;color:var(--muted)}

.cards{position:absolute;top:1208px;left:52px;width:1096px;height:512px}
.card{position:absolute;padding:30px 30px}
.card h3{font-family:"Playfair Display",serif;font-weight:500;font-size:26px;line-height:1.2;margin-bottom:10px}
.card p{font-size:11px;line-height:1.55;color:var(--muted)}
.card-cert{left:0;top:0;width:352px;height:252px;background:var(--sage);display:flex;flex-direction:column;justify-content:flex-end}
.card-cert h3{font-size:22px}
.card-tech{left:372px;top:0;width:724px;height:252px;background:var(--cream-2);display:flex;flex-direction:column;justify-content:flex-end}
.card-chain{left:0;top:264px;width:740px;height:248px;background:var(--cream-2);display:flex;flex-direction:column;justify-content:flex-end}
.card-4pl{left:760px;top:264px;width:336px;height:248px;background:var(--brown);color:var(--white);display:flex;flex-direction:column;justify-content:flex-end}
.card-4pl p{color:#e8d8c6}
.card-icon{position:absolute;top:28px;left:30px}
.card-tech .card-icon{left:auto;right:30px}
.chip{position:absolute;top:28px;left:30px;display:flex;align-items:center;gap:8px}

/* integrity */
.integrity{position:absolute;top:1832px;left:0;width:1200px;height:640px}
.photo-meat{position:absolute;left:52px;top:0;width:500px;height:620px;background:radial-gradient(circle at 70% 30%,#c63a35 0%,#a8483e 25%,#8c3a30 55%,#5a231c 100%)}
.photo-inset{position:absolute;left:385px;top:456px;width:206px;height:184px;background:radial-gradient(circle at 50% 50%,#9fd3d6 0%,#2d6a72 30%,#0e1e24 70%);border:4px solid var(--cream)}
.integrity-copy{position:absolute;left:645px;top:26px;width:500px}
.integrity-copy h2{font-family:"Playfair Display",serif;font-weight:500;font-size:38px;line-height:1.15;margin:14px 0 22px}
.integrity-copy > p{font-size:13px;line-height:1.65;color:var(--muted);margin-bottom:26px}
.step{display:flex;gap:18px;margin-bottom:20px}
.step-num{font-size:10px;font-weight:700;color:var(--brown);width:14px}
.step h4{font-size:9px;letter-spacing:.16em;font-weight:700;margin-bottom:4px}
.step p{font-size:11px;line-height:1.5;color:var(--muted)}

/* hubs */
.hubs{position:absolute;top:2590px;left:0;width:1200px;text-align:center}
.hubs h2{font-family:"Playfair Display",serif;font-weight:500;font-size:30px;line-height:1.2;color:var(--brown-dark)}
.hub-list{display:flex;justify-content:center;gap:300px;margin-top:52px}
.hub h3{font-family:"Playfair Display",serif;font-weight:500;font-size:24px}
.hub span{display:block;font-size:8px;letter-spacing:.16em;font-weight:700;color:var(--muted);margin-top:6px}
.map{position:absolute;top:2800px;left:0;width:1200px;height:365px;background:linear-gradient(180deg,#2b4a48 0%,#1d3533 100%)}
.map svg{position:absolute;left:258px;top:78px}

/* footer */
.site-footer{position:absolute;top:3165px;left:0;width:1200px;height:383px;background:var(--cream)}
.footer-brand{position:absolute;left:108px;top:100px;width:320px}
.footer-brand .brand{font-size:20px}
.footer-brand p{font-size:11px;line-height:1.6;color:var(--muted);margin:16px 0 18px}
.socials{display:flex;gap:10px}
.socials span{width:26px;height:26px;border-radius:50%;background:var(--line);display:block}
.footer-col{position:absolute;top:100px;font-size:11px;line-height:1.55;color:var(--muted)}
.footer-col h5{font-size:9px;letter-spacing:.16em;font-weight:700;color:var(--ink);margin-bottom:14px}
.footer-col li{list-style:none;margin-bottom:10px;width:90px}
.copyright{position:absolute;bottom:22px;left:0;width:1200px;text-align:center;font-size:9px;color:var(--muted);letter-spacing:.06em}
</style>
</head>
<body>

<header class="site-nav">
  <div class="brand">TARQUEL</div>
  <nav class="nav-links">
    <span class="active">Pet Food</span><span>Agri-Food</span><span>Technology</span><span>Sustainability</span>
  </nav>
  <div class="nav-cta">Contact Us</div>
</header>

<section class="hero">
  <div class="hero-pane hero-pet" role="img" aria-label="Golden retriever beside fresh raw meat and berries">
    <div class="eyebrow">Explore Pet</div>
    <h1>Pet Food<br>Raw Nutrition</h1>
    <div class="btn-light">Explore Pet Food</div>
  </div>
  <div class="hero-pane hero-agri" role="img" aria-label="Industrial freeze-drying chamber in a clean laboratory">
    <div class="eyebrow">Explore Agri</div>
    <h1>Agri-Food<br>Industrial Solutions</h1>
    <div class="btn-dark">Explore Agri-Food</div>
  </div>
</section>

<section class="difference">
  <div class="eyebrow">Technical Mastery</div>
  <h2>The Tarquel Difference:<br>Scientific Purity &amp; Scale</h2>
  <p>Leveraging advanced sublimation technology to preserve nature's structural integrity with clinical precision.</p>
</section>

<section class="cards">
  <article class="card card-cert">
    <svg class="card-icon" width="18" height="20" viewBox="0 0 18 20"><path d="M9 1 L16 4 V10 C16 14 13 17 9 19 C5 17 2 14 2 10 V4 Z" fill="none" stroke="#4a2a12" stroke-width="1.5"/><path d="M6 10 L8.5 12.5 L12.5 8" fill="none" stroke="#4a2a12" stroke-width="1.5"/></svg>
    <h3>CFIA &amp; Health<br>Canada Certified</h3>
    <p>Strict adherence to national safety protocols and pharmaceutical-grade hygiene standards.</p>
  </article>
  <article class="card card-tech">
    <svg class="card-icon" width="22" height="22" viewBox="0 0 22 22"><path d="M4 18 L10 8 M8 4 L14 10 M12 18 H20 M14 14 L18 18" fill="none" stroke="#4a2a12" stroke-width="1.6"/></svg>
    <h3>Proprietary Sublimation Tech</h3>
    <p>Our unique low-temperature cycle maintains 99% of nutritional bioavailability and cellular structure.</p>
  </article>
  <article class="card card-chain">
    <div class="chip"><svg width="14" height="14" viewBox="0 0 14 14"><circle cx="7" cy="7" r="6" fill="none" stroke="#6b3f1d" stroke-width="1.4"/></svg><span class="eyebrow" style="font-size:8px">Climate Integrity</span></div>
    <h3>End-to-End Cold Chain</h3>
    <p>A seamless thermal corridor from harvest to freeze-drying, ensuring zero ingredient degradation.</p>
  </article>
  <article class="card card-4pl">
    <svg class="card-icon" width="20" height="20" viewBox="0 0 20 20"><path d="M10 1 V19 M1 10 H19 M3.5 3.5 L16.5 16.5 M16.5 3.5 L3.5 16.5" stroke="#f3e6d6" stroke-width="1.4"/></svg>
    <h3>4PL Supply Chain</h3>
    <p>Full service logistics integration for industrial partners, managing global distribution and storage.</p>
  </article>
</section>

<section class="integrity">
  <div class="photo-meat" role="img" aria-label="Close-up of marbled raw meat with fresh strawberries"></div>
  <div class="photo-inset" role="img" aria-label="Macro view of a glowing lab lens"></div>
  <div class="integrity-copy">
    <div class="eyebrow">Technical Integrity</div>
    <h2>Where Raw Integrity<br>Meets Lab Precision</h2>
    <p>At TARQUEL, we treat ingredients as biological masterpieces. Our process isn't just about manufacturing—it's about the microscopic preservation of nature's nutritional design through intentional engineering.</p>
    <div class="step"><span class="step-num">01</span><div><h4>FLASH FREEZING</h4><p>Immediate moisture immobilization at -40°C to prevent ice crystal formation.</p></div></div>
    <div class="step"><span class="step-num">02</span><div><h4>VACUUM SUBLIMATION</h4><p>Gentle extraction of water vapor without liquid phase transition.</p></div></div>
    <div class="step"><span class="step-num">03</span><div><h4>STRUCTURAL ANALYSIS</h4><p>Batch testing for nutrient density and cellular structural integrity.</p></div></div>
  </div>
</section>

<section class="hubs">
  <h2>Manufacturing<br>Hubs</h2>
  <div class="hub-list">
    <div class="hub"><h3>Edmonton, AB</h3><span>PRIMARY PROCESSING</span></div>
    <div class="hub"><h3>Kelowna, BC</h3><span>STRATEGIC LOCATION</span></div>
  </div>
</section>

<div class="map" role="img" aria-label="Dark map of Western Canada marking the two manufacturing hubs">
  <svg width="26" height="34" viewBox="0 0 26 34"><path d="M13 1 C6 1 1 6 1 13 C1 22 13 33 13 33 C13 33 25 22 25 13 C25 6 20 1 13 1 Z" fill="#f3ebe3"/><circle cx="13" cy="13" r="4.5" fill="#1f3b3a"/></svg>
</div>

<footer class="site-footer">
  <div class="footer-brand">
    <div class="brand">TARQUEL</div>
    <p>Precision preservation for the next generation of nutrition. From raw industrial ingredients to high-end pet food solutions.</p>
    <div class="socials"><span></span><span></span></div>
  </div>
  <div class="footer-col" style="left:720px">
    <h5>SOLUTIONS</h5>
    <ul><li>Pet Food Solutions</li><li>Agri-Food Industrial</li><li>B2B Portal</li></ul>
  </div>
  <div class="footer-col" style="left:960px">
    <h5>COMPANY</h5>
    <ul><li>Science</li><li>Utility Report</li><li>Quality Certifications</li><li>Contact</li></ul>
  </div>
  <div class="copyright">© 2024 TARQUEL Foods Inc. Precision Preservation.</div>
</footer>

</body>
</html>
```